International Food Manufacturer in the need of a new business card and logo.

Our Company - Brightfield Provisions Ltd.

Our Industry - Food and Drink

We are a Wild Harvested Food Distributor / Manufacturer. We service the following food sectors: Supermarkets, Hotels, Restaurants, Cafes, Catering and all people looking to eat healthy food products.

Slogan - The finest source for all things wholesome

Business card details -

48-52 Quarrow Lane
Ashby Meadow
London
NP7 3RD United Kingdom
Morven Tillick
+44 7700 900412 - UK
+971 50 5550137 - UAE
+38 067 555 0198 - Ukraine
morven@brightfieldprovisions.com
www.brightfieldprovisions.com

Goal - We are looking for a dynamic modern new look for our corporate image and a designer who can bring this new concept to our future food product designs. Please try to incorporate 3d hexagonal vector Imaging in your design concepts.

Target Market(s)

Industry/Entity Type

Food Service

Contact Information for Business Card

Brightfield Provisions Ltd.
48-52 Quarrow Lane
Ashby Meadow
London
NP7 3RD United Kingdom
Morven Tillick
+44 7700 900412 - UK
+971 50 5550137 - UAE

Font styles to use
Serif

Colors

Designer to choose colors to be used in the design.

Requirements
Must have
• Please read project description above.
Nice to have
Should not have

```html
<!DOCTYPE html>
<html lang="en">
<head>
<meta charset="utf-8">
<title>Brightfield Provisions Ltd. — Business Card</title>
<link rel="stylesheet" href="https://fonts.googleapis.com/css2?family=Lato:wght@400;700&family=Oswald:wght@500&display=swap">
<style>
  :root {
    --backdrop: #4a403b;
    --card: #0d0d0d;
    --orange: #f57c1f;
    --green: #8cd92a;
    --white: #f2f2f2;
    --silver: #bdbdbd;
    --divider: #3a3a3a;
  }
  * { margin: 0; padding: 0; box-sizing: border-box; }
  html, body { width: 1200px; height: 900px; overflow: hidden; }
  body {
    background: var(--backdrop);
    font-family: "Lato", sans-serif;
    display: flex;
    align-items: center;
    justify-content: center;
    gap: 40px;
  }
  .card {
    width: 540px;
    height: 309px;
    background: var(--card);
    border-radius: 3px;
    position: relative;
    box-shadow: 0 12px 30px rgba(0,0,0,0.45);
  }
  /* front */
  .card-front { display: flex; }
  .brand-block {
    width: 230px;
    display: flex;
    align-items: center;
    justify-content: center;
    gap: 10px;
    padding-left: 18px;
  }
  .brand-dot {
    width: 16px; height: 16px;
    border-radius: 50%;
    background: var(--green);
    flex: none;
  }
  .brand-name {
    font-family: "Lato", sans-serif;
    font-weight: 700;
    font-size: 21px;
    line-height: 1.15;
    color: var(--green);
  }
  .contact-block {
    border-left: 1px solid var(--divider);
    margin: 34px 0;
    padding-left: 16px;
    display: flex;
    flex-direction: column;
    justify-content: center;
  }
  .person-name {
    font-family: "Oswald", sans-serif;
    font-weight: 500;
    font-size: 24px;
    text-transform: uppercase;
    letter-spacing: 0.2px;
    margin-bottom: 8px;
  }
  .person-name .first { color: var(--orange); }
  .person-name .last { color: var(--green); }
  .contact-line {
    display: flex;
    align-items: center;
    gap: 7px;
    color: var(--white);
    font-size: 14px;
    line-height: 19px;
  }
  .contact-line svg { width: 11px; height: 11px; fill: var(--orange); flex: none; }
  .region { color: var(--green); }
  .company {
    color: var(--orange);
    font-size: 15px;
    line-height: 20px;
    margin-top: 6px;
  }
  .address { color: var(--white); font-size: 15px; line-height: 20px; }
  /* back */
  .card-back {
    display: flex;
    flex-direction: column;
    align-items: center;
    justify-content: center;
    text-align: center;
  }
  .back-name {
    font-family: "Lato", sans-serif;
    font-weight: 700;
    font-size: 28px;
    letter-spacing: 0.5px;
    text-transform: uppercase;
    color: var(--silver);
    display: flex;
    align-items: center;
    gap: 12px;
  }
  .back-dot {
    width: 18px; height: 18px;
    border-radius: 50%;
    background: var(--silver);
  }
  .slogan {
    margin-top: 18px;
    font-size: 13px;
    letter-spacing: 0.6px;
    text-transform: uppercase;
    color: var(--silver);
  }
</style>
</head>
<body>
  <section class="card card-front">
    <div class="brand-block">
      <span class="brand-dot"></span>
      <span class="brand-name">Brightfield<br>Provisions</span>
    </div>
    <div class="contact-block">
      <h1 class="person-name"><span class="first">Morven</span> <span class="last">Tillick</span></h1>
      <p class="contact-line"><svg viewBox="0 0 12 12"><path d="M2 1h2.5l1 2.6-1.4 1a6 6 0 0 0 3.3 3.3l1-1.4L11 7.5V10a1 1 0 0 1-1 1A9 9 0 0 1 1 2a1 1 0 0 1 1-1z"/></svg>+44 7700 900412 <span class="region">(UK)</span></p>
      <p class="contact-line"><svg viewBox="0 0 12 12"><path d="M2 1h2.5l1 2.6-1.4 1a6 6 0 0 0 3.3 3.3l1-1.4L11 7.5V10a1 1 0 0 1-1 1A9 9 0 0 1 1 2a1 1 0 0 1 1-1z"/></svg>+971 50 5550137 <span class="region">(UAE)</span></p>
      <p class="contact-line"><svg viewBox="0 0 12 12"><path d="M2 1h2.5l1 2.6-1.4 1a6 6 0 0 0 3.3 3.3l1-1.4L11 7.5V10a1 1 0 0 1-1 1A9 9 0 0 1 1 2a1 1 0 0 1 1-1z"/></svg>+38 067 555 0198 <span class="region">(Ukraine)</span></p>
      <p class="contact-line"><svg viewBox="0 0 12 12"><path d="M1 2.5h10v7H1z M1 2.5l5 4 5-4" stroke="#0d0d0d" stroke-width="1"/></svg>morven@brightfieldprovisions.com</p>
      <p class="contact-line"><svg viewBox="0 0 12 12"><circle cx="6" cy="6" r="5"/><path d="M1 6h10M6 1c-2.5 3-2.5 7 0 10M6 1c2.5 3 2.5 7 0 10" stroke="#0d0d0d" stroke-width="0.9" fill="none"/></svg>www.brightfieldprovisions.com</p>
      <p class="company">Brightfield Provisions Ltd.</p>
      <p class="address">48-52 Quarrow Lane<br>Ashby Meadow London<br>NP7 3RD United Kingdom</p>
    </div>
  </section>

  <section class="card card-back">
    <h2 class="back-name"><span class="back-dot"></span>Brightfield Provisions Ltd.</h2>
    <p class="slogan">The finest source for all things wholesome</p>
  </section>
</body>
</html>
```